Illustration Design Project - Memory

We need a cool simpe visual that shows our training methodology (for business training programmes) - moving information from short term to long term memory.
The art needs to be simple and impactful - and will could include reference to our training company - Brightlane - http://www.brightlane.co.uk

A more detailed idea of the 7 step process we use for achieving this movement from short to long term memory can be found at http://www.learnharbor.com/b_topic/staffdev/staffdev284c.shtml

The final design should be fun, slick and simple. It should feel like a PROCESS if possible.

Industry/Entity Type

Training

Requirements
Must have
• Process feel.
Should not have
• Should not have too many colours.

```html
<!DOCTYPE html>
<html lang="en">
<head>
<meta charset="utf-8">
<title>Brightlane's Pedagogy</title>
<link rel="stylesheet" href="https://fonts.googleapis.com/css2?family=Righteous&family=Open+Sans:wght@700&family=Fira+Sans+Condensed:wght@600&display=swap">
<style>
  :root {
    --bg-centre: #fdf4dc;
    --bg-edge: #f5dba6;
    --brick: #b5533c;
    --link-line: #a85a45;
    --brand-square: #8b3a45;
    --brand-text: #3d5a86;
    --step-reach: #ffd200;
    --step-reflect: #fcb62a;
    --step-recode: #f99b34;
    --step-reinforce: #f08a21;
    --step-rehearse: #ee8e26;
    --step-review: #d1701d;
    --step-retrieve: #b14f40;
    --label-dark: #6a1d0f;
    --label-light: #fde7c2;
    --figure-tone: #f3c3b2;
  }
  html, body {
    margin: 0;
    padding: 0;
    overflow: hidden;
  }
  .canvas {
    position: relative;
    width: 1200px;
    height: 752px;
    overflow: hidden;
    background: radial-gradient(ellipse at 45% 40%, var(--bg-centre) 0%, #f9e8c2 55%, var(--bg-edge) 100%);
  }
  .title {
    position: absolute;
    left: 228px;
    top: 44px;
    margin: 0;
    font-family: "Righteous", sans-serif;
    font-weight: 400;
    font-size: 46px;
    letter-spacing: 1px;
    color: var(--brick);
  }
  .brand {
    position: absolute;
    left: 1040px;
    top: 33px;
    width: 120px;
    text-align: center;
  }
  .brand-square {
    width: 92px;
    height: 78px;
    margin: 0 auto;
    background: var(--brand-square);
  }
  .brand-name {
    margin-top: 10px;
    font-family: "Open Sans", sans-serif;
    font-weight: 700;
    font-size: 17px;
    color: var(--brand-text);
  }
  .process {
    position: absolute;
    left: 0;
    top: 0;
  }
  .step-label {
    font-family: "Open Sans", sans-serif;
    font-weight: 700;
    font-size: 17px;
    text-anchor: middle;
    dominant-baseline: central;
  }
  .equals-bar {
    position: absolute;
    left: 526px;
    width: 87px;
    height: 17px;
    background: var(--brick);
  }
  .equals-bar.top { top: 430px; }
  .equals-bar.bottom { top: 466px; }
  .reminder-figure {
    position: absolute;
    left: 873px;
    top: 319px;
    width: 147px;
    height: 222px;
    border-radius: 40px 40px 8px 8px;
    background: linear-gradient(180deg, #fbe3d6 0%, var(--figure-tone) 100%);
  }
  .ground-line {
    position: absolute;
    left: 727px;
    top: 585px;
    width: 381px;
    height: 3px;
    background: var(--brick);
  }
  .caption {
    position: absolute;
    left: 623px;
    top: 606px;
    margin: 0;
    font-family: "Fira Sans Condensed", sans-serif;
    font-weight: 600;
    font-size: 24px;
    color: var(--brick);
    white-space: nowrap;
  }
</style>
</head>
<body>
<main class="canvas">
  <h1 class="title">BRIGHTLANE’S PEDAGOGY</h1>

  <div class="brand">
    <div class="brand-square"></div>
    <div class="brand-name">Brightlane</div>
  </div>

  <svg class="process" width="1200" height="752" viewBox="0 0 1200 752" aria-label="Seven step learning cycle">
    <polygon points="265,315 377,370 403,493 327,587 203,587 124,491 149,368"
             fill="none" stroke="var(--link-line)" stroke-width="5"/>
    <g class="step">
      <circle cx="265" cy="315" r="55" fill="var(--step-reach)"/>
      <text class="step-label" x="265" y="315" fill="var(--label-dark)">Reach</text>
    </g>
    <g class="step">
      <circle cx="377" cy="370" r="55" fill="var(--step-reflect)"/>
      <text class="step-label" x="377" y="370" fill="var(--label-dark)">Reflect</text>
    </g>
    <g class="step">
      <circle cx="403" cy="493" r="55" fill="var(--step-recode)"/>
      <text class="step-label" x="403" y="493" fill="var(--label-dark)">Recode</text>
    </g>
    <g class="step">
      <circle cx="327" cy="587" r="55" fill="var(--step-reinforce)"/>
      <text class="step-label" x="327" y="587" fill="var(--label-dark)">Reinforce</text>
    </g>
    <g class="step">
      <circle cx="203" cy="587" r="55" fill="var(--step-rehearse)"/>
      <text class="step-label" x="203" y="587" fill="var(--label-light)">Rehearse</text>
    </g>
    <g class="step">
      <circle cx="124" cy="491" r="55" fill="var(--step-review)"/>
      <text class="step-label" x="124" y="491" fill="var(--label-light)">Review</text>
    </g>
    <g class="step">
      <circle cx="149" cy="368" r="55" fill="var(--step-retrieve)"/>
      <text class="step-label" x="149" y="368" fill="var(--label-light)">Retrieve</text>
    </g>
  </svg>

  <div class="equals-bar top"></div>
  <div class="equals-bar bottom"></div>

  <div class="reminder-figure" role="img" aria-label="Cartoon character holding up a giant pointing finger tied with a red reminder string"></div>
  <div class="ground-line"></div>

  <p class="caption">Moving Learning into the Long Term Memory</p>
</main>
</body>
</html>
```